Header Design

I would like a new header design for my website - www.nestmarlo.com.

I am a Realtor and the header should reflect that and complement the theme.

The attached logo needs to be included and the information that is already there. Also, the colors need to match.

Marlo Quinby
Connecting you to the Los Angeles real estate scene.

Industry/Entity Type

Realtor

```html
<!DOCTYPE html>
<html lang="en">
<head>
<meta charset="utf-8">
<title>Marlo Quinby – Header</title>
<link rel="stylesheet" href="https://fonts.googleapis.com/css2?family=Open+Sans:wght@700&display=swap">
<style>
  :root {
    --brand-bg: #2b1c30;
    --brand-ink: #ffffff;
    --sky-top: #3b3f86;
    --sky-mid: #5b5ea8;
    --horizon: #2a2c5a;
    --city-glow: #c98a3a;
    --city-dark: #1c1d3a;
    --title-ink: #ecd63c;
    --tagline: #ecd63c;
  }
  html, body {
    margin: 0;
    padding: 0;
    overflow: hidden;
    background: #ffffff;
  }
  .header {
    position: relative;
    width: 1200px;
    height: 125px;
    overflow: hidden;
    background: var(--brand-bg);
  }
  .brand-block {
    position: absolute;
    left: 0;
    top: 0;
    width: 181px;
    height: 125px;
    background: var(--brand-bg);
    display: flex;
    flex-direction: column;
    align-items: center;
    justify-content: center;
    gap: 8px;
  }
  .brand-mark {
    width: 22px;
    height: 22px;
    background: var(--brand-ink);
  }
  .brand-name {
    font-family: "Open Sans", sans-serif;
    font-weight: 700;
    font-size: 15px;
    color: var(--brand-ink);
    letter-spacing: 0.5px;
  }
  .skyline {
    position: absolute;
    left: 181px;
    top: 0;
    width: 1019px;
    height: 125px;
    background:
      radial-gradient(ellipse 60% 30% at 55% 100%, var(--city-glow) 0%, transparent 70%),
      linear-gradient(to bottom, var(--sky-top) 0%, var(--sky-mid) 45%, var(--horizon) 75%, var(--city-dark) 100%);
  }
  .title {
    position: absolute;
    left: 283px;
    top: 8px;
    margin: 0;
    font-family: "Open Sans", sans-serif;
    font-weight: 700;
    font-size: 44px;
    line-height: 1.2;
    color: var(--title-ink);
  }
  .tagline {
    position: absolute;
    left: 331px;
    top: 80px;
    margin: 0;
    font-family: "Open Sans", sans-serif;
    font-weight: 700;
    font-size: 18px;
    color: var(--tagline);
    text-shadow: 1px 1px 1px rgba(0,0,0,0.5);
  }
</style>
</head>
<body>
  <header class="header">
    <div class="brand-block">
      <span class="brand-mark"></span>
      <span class="brand-name">Marlo Quinby</span>
    </div>
    <div class="skyline" role="img" aria-label="Night view of the Los Angeles skyline with lit towers and city lights under a purple sky"></div>
    <h1 class="title">Marlo Quinby</h1>
    <p class="tagline">Connecting you to the Los Angeles real estate scene.</p>
  </header>
</body>
</html>
```